Flu 2019

Lockridge Regional Hospital is hosting a health fair/flu shot clinic this Fall. What she'd like to convey is the following:

Health Fair & Flu Clinic 2019
At the following locations from 10am - 1pm
Cedar Bluff - September 25 at Courthouse in Cedar Bluff
Eden - October 2 at Harlow Multipurpose Center
Menard - October 9 at Tasker Community Center
No cost flu shots available. Please bring insurance information.
Door prizes - Giveaways - Treats
Brought to you by Lockridge Regional Hospital

We would like to highlight the health fair which will be free to the community. We would like to also highlight the flu clinic; however, the no cost/bring insurance needs to be in smaller print.

```html
<!DOCTYPE html>
<html lang="en">
<head>
<meta charset="UTF-8">
<title>Lockridge Regional Hospital — 2019 Health Fair and Flu Clinic</title>
<link href="https://fonts.googleapis.com/css2?family=Bebas+Neue&family=Abel&display=swap" rel="stylesheet">
<style>
  :root {
    --paper: #efeff0;
    --paper-light: #fafafa;
    --ink: #111111;
    --brand-blue: #1f63ae;
    --card: #ffffff;
    --shadow: rgba(0, 0, 0, 0.14);
  }
  * { margin: 0; padding: 0; box-sizing: border-box; }
  html, body { width: 848px; height: 1200px; overflow: hidden; }
  body {
    background: #ffffff;
    font-family: "Abel", sans-serif;
    color: var(--ink);
  }
  .poster {
    position: relative;
    width: 848px;
    height: 1200px;
    overflow: hidden;
    background:
      radial-gradient(ellipse at 70% 80%, #ffffff 0%, rgba(255,255,255,0) 45%),
      radial-gradient(ellipse at 20% 60%, #f7f7f8 0%, rgba(247,247,248,0) 50%),
      linear-gradient(160deg, var(--paper-light) 0%, var(--paper) 55%, #e9e9eb 100%);
  }
  .brand-tab {
    position: absolute;
    left: 0; top: 0;
    width: 370px; height: 194px;
    filter: drop-shadow(0 3px 6px var(--shadow));
  }
  .brand-name {
    position: absolute;
    left: 40px; top: 32px;
    width: 250px;
    font-family: "Abel", sans-serif;
    font-size: 34px;
    line-height: 38px;
    color: var(--ink);
  }
  .hero-photo {
    position: absolute;
    left: 270px; top: -8px;
    width: 590px; height: 668px;
  }
  .headline {
    position: absolute;
    left: 30px; top: 262px;
    font-family: "Bebas Neue", sans-serif;
  }
  .headline-year {
    display: block;
    font-size: 92px;
    line-height: 92px;
    color: var(--ink);
    margin-bottom: 8px;
  }
  .headline-event {
    display: block;
    font-size: 66px;
    line-height: 78px;
    color: var(--brand-blue);
  }
  .schedule-intro {
    position: absolute;
    left: 0; top: 694px;
    width: 848px;
    text-align: center;
    font-size: 25px;
    color: var(--ink);
  }
  .venues {
    position: absolute;
    left: 98px; top: 762px;
    display: flex;
    gap: 30px;
  }
  .venue-card {
    width: 196px;
    height: 178px;
    background: var(--card);
    border-radius: 14px;
    box-shadow: 0 2px 8px var(--shadow);
    text-align: center;
    padding-top: 20px;
  }
  .venue-date {
    font-family: "Bebas Neue", sans-serif;
    font-size: 30px;
    line-height: 34px;
    color: var(--brand-blue);
    margin-bottom: 12px;
  }
  .venue-place {
    font-size: 26px;
    line-height: 32px;
    color: var(--ink);
  }
  .pin {
    width: 12px; height: 16px;
    vertical-align: 2px;
    margin-right: 6px;
  }
  .perks {
    position: absolute;
    left: 0; top: 988px;
    width: 848px;
    text-align: center;
    font-family: "Bebas Neue", sans-serif;
    font-size: 52px;
    line-height: 56px;
    color: var(--ink);
    letter-spacing: 0.5px;
  }
  .fine-print {
    position: absolute;
    left: 0; top: 1078px;
    width: 848px;
    text-align: center;
    font-size: 26px;
    line-height: 38px;
    color: var(--ink);
  }
</style>
</head>
<body>
<main class="poster">

  <svg class="brand-tab" viewBox="0 0 370 194" aria-hidden="true">
    <polygon points="0,0 370,0 300,194 0,194" fill="#ffffff"/>
  </svg>
  <div class="brand-name">Lockridge Regional Hospital</div>

  <svg class="hero-photo" viewBox="0 0 590 668" role="img" aria-label="Photo of a smiling mother cuddling her blue-eyed baby outdoors">
    <defs>
      <linearGradient id="photoTone" x1="0" y1="0" x2="1" y2="1">
        <stop offset="0" stop-color="#c9b48f"/>
        <stop offset="0.35" stop-color="#e8c2aa"/>
        <stop offset="0.7" stop-color="#f2d6c8"/>
        <stop offset="1" stop-color="#d9d3c4"/>
      </linearGradient>
      <filter id="photoShadow" x="-5%" y="-5%" width="110%" height="110%">
        <feDropShadow dx="0" dy="3" stdDeviation="5" flood-color="#000" flood-opacity="0.2"/>
      </filter>
    </defs>
    <polygon points="0,226 228,-2 600,-2 600,540 472,668 0,668" fill="#ffffff" filter="url(#photoShadow)"/>
    <polygon points="8,230 232,8 590,8 590,536 466,658 8,658" fill="url(#photoTone)"/>
  </svg>

  <h1 class="headline">
    <span class="headline-year">2019</span>
    <span class="headline-event">Health</span>
    <span class="headline-event">Fair and</span>
    <span class="headline-event">Flu Clinic</span>
  </h1>

  <p class="schedule-intro">at the following locations from 10am - 1pm</p>

  <section class="venues">
    <div class="venue-card">
      <div class="venue-date">September 25</div>
      <div class="venue-place">
        <svg class="pin" viewBox="0 0 12 16" aria-hidden="true"><path d="M6 0C2.7 0 0 2.6 0 5.8 0 10 6 16 6 16s6-6 6-10.2C12 2.6 9.3 0 6 0zm0 8.2a2.4 2.4 0 1 1 0-4.8 2.4 2.4 0 0 1 0 4.8z" fill="var(--brand-blue)"/></svg>Courthouse<br>in Cedar Bluff
      </div>
    </div>
    <div class="venue-card">
      <div class="venue-date">October 2</div>
      <div class="venue-place">
        <svg class="pin" viewBox="0 0 12 16" aria-hidden="true"><path d="M6 0C2.7 0 0 2.6 0 5.8 0 10 6 16 6 16s6-6 6-10.2C12 2.6 9.3 0 6 0zm0 8.2a2.4 2.4 0 1 1 0-4.8 2.4 2.4 0 0 1 0 4.8z" fill="var(--brand-blue)"/></svg>Harlow Purpose<br>Center
      </div>
    </div>
    <div class="venue-card">
      <div class="venue-date">October 9</div>
      <div class="venue-place">
        <svg class="pin" viewBox="0 0 12 16" aria-hidden="true"><path d="M6 0C2.7 0 0 2.6 0 5.8 0 10 6 16 6 16s6-6 6-10.2C12 2.6 9.3 0 6 0zm0 8.2a2.4 2.4 0 1 1 0-4.8 2.4 2.4 0 0 1 0 4.8z" fill="var(--brand-blue)"/></svg>Tasker<br>Community Center
      </div>
    </div>
  </section>

  <p class="perks">Door Prizes • Giveaways • Treats</p>

  <p class="fine-print">No cost flu shots available.<br>Please bring insurance information.</p>

</main>
</body>
</html>
```